Create a Branded Four Stage Lifecycle Diagram

We need a rethink / redesign of our Lifecycle. We created it and have used it till now but it is not professional and needs our branding as well. We use it for presentations, for analysis with schools when we are consulting on site and it should look equally good on a powerpoint slide as on a handout and, of course, as a JPG that we can copy onto documents that we create. It does not have to look like what we currently have. I will include the article so you can see what we are trying to achieve. Eventually we want to be able to trademark it. It should include copyright 2020 Harbor Academy Advisors. Each stafe should reflect its characteristics in some fashion.

Target Market(s)

We serve K-12 Christian private schools

Industry/Entity Type

Education

Font styles to use
Sans Serif

Colors

Designer to choose colors to be used in the design.

Requirements
Must have
• HAA logo
• copyright notice
• title: HAA Lifecycle
Nice to have
• In the article, you will see the Corporate Lifecycle. It is completely different from ours. You will also see our current 'design'. It does not have to be like the one we currently have - it is not a refresh - it is a new design.
Should not have
• There must be no chance that our design could be confused with the corporate lifecycle.

```html
<!DOCTYPE html>
<html lang="en">
<head>
<meta charset="utf-8">
<title>HAA Lifecycle</title>
<link rel="stylesheet" href="https://fonts.googleapis.com/css2?family=Cormorant+Garamond:wght@500&family=Marcellus&family=Open+Sans:wght@600&display=swap">
<style>
  :root {
    --brand-blue: #0a72ad;
    --chevron-blue: #2b9ed2;
    --title-grey: #707070;
    --number-grey: #6f6f6f;
    --ink: #1a1a1a;
    --paper: #ffffff;
  }
  html, body {
    margin: 0;
    padding: 0;
    width: 982px;
    height: 1200px;
    overflow: hidden;
    background: var(--paper);
  }
  .lifecycle-sheet {
    display: block;
    width: 982px;
    height: 1200px;
  }
  .brand-name {
    font-family: "Marcellus", serif;
    font-size: 26px;
    letter-spacing: 0.5px;
    fill: var(--brand-blue);
    text-anchor: middle;
  }
  .diagram-title {
    font-family: "Marcellus", serif;
    font-size: 40px;
    letter-spacing: 1px;
    text-anchor: middle;
  }
  .diagram-title--blue { fill: var(--brand-blue); }
  .diagram-title--grey { fill: var(--title-grey); }
  .stage-years {
    font-family: "Cormorant Garamond", serif;
    font-weight: 500;
    font-size: 32px;
    font-variant-numeric: lining-nums;
    fill: var(--number-grey);
    text-anchor: middle;
  }
  .stage-label {
    font-family: "Marcellus", serif;
    font-size: 22px;
    letter-spacing: 0.5px;
    fill: var(--paper);
  }
  .copyright-note {
    font-family: "Open Sans", sans-serif;
    font-weight: 600;
    font-size: 10px;
    fill: var(--ink);
    text-anchor: middle;
  }
  .stage-disc { filter: url(#disc-shadow); }
  .chevron {
    fill: none;
    stroke: var(--chevron-blue);
    stroke-width: 7;
    stroke-linecap: round;
    stroke-linejoin: round;
  }
</style>
</head>
<body>
<svg class="lifecycle-sheet" viewBox="0 0 1300 1589" xmlns="http://www.w3.org/2000/svg">
  <defs>
    <linearGradient id="band-fade" x1="260" y1="0" x2="1015" y2="0" gradientUnits="userSpaceOnUse">
      <stop offset="0" stop-color="#0a6da8"/>
      <stop offset="0.5" stop-color="#1a84bb"/>
      <stop offset="1" stop-color="#4a9dc8"/>
    </linearGradient>
    <radialGradient id="disc-fill" cx="0.45" cy="0.3" r="0.8">
      <stop offset="0" stop-color="#ffffff"/>
      <stop offset="0.6" stop-color="#f1f1f1"/>
      <stop offset="1" stop-color="#dcdcdc"/>
    </radialGradient>
    <filter id="disc-shadow" x="-30%" y="-30%" width="160%" height="170%">
      <feDropShadow dx="0" dy="9" stdDeviation="7" flood-color="#000" flood-opacity="0.22"/>
    </filter>
    <path id="wave-line" d="M 276 595 A 90 90 0 0 0 456 595 A 90 90 0 0 1 636 595 A 90 90 0 0 0 816 595 A 90 90 0 0 1 996 595"/>
    <path id="arc-entrepreneur" d="M 276 595 A 90 90 0 0 0 456 595"/>
    <path id="arc-adolescent" d="M 456 595 A 90 90 0 0 1 636 595"/>
    <path id="arc-mature" d="M 636 595 A 90 90 0 0 0 816 595"/>
    <path id="arc-dying" d="M 816 595 A 90 90 0 0 1 996 595"/>
  </defs>

  <!-- Version one: gradient band -->
  <g class="lifecycle-panel">
    <text class="brand-name" x="642" y="385">Harbor Academy Advisors</text>
    <text class="diagram-title diagram-title--blue" x="642" y="452">HAA LIFECYCLE</text>

    <use href="#wave-line" fill="none" stroke="url(#band-fade)" stroke-width="35" stroke-linecap="round"/>

    <g class="stage-disc">
      <circle cx="366" cy="595" r="72" fill="url(#disc-fill)"/>
      <circle cx="546" cy="595" r="72" fill="url(#disc-fill)"/>
      <circle cx="727" cy="595" r="72" fill="url(#disc-fill)"/>
      <circle cx="906" cy="595" r="72" fill="url(#disc-fill)"/>
    </g>

    <text class="stage-years" x="366" y="598">0-10</text>
    <text class="stage-years" x="366" y="621">years</text>
    <text class="stage-years" x="546" y="597">10-15</text>
    <text class="stage-years" x="546" y="620">years</text>
    <text class="stage-years" x="728" y="597">15-30</text>
    <text class="stage-years" x="728" y="620">years</text>
    <text class="stage-years" x="907" y="592">20</text>
    <text class="stage-years" x="907" y="615">years+</text>

    <text class="stage-label" dominant-baseline="central"><textPath href="#arc-entrepreneur" startOffset="50%" text-anchor="middle">ENTREPRENEUR</textPath></text>
    <text class="stage-label" dominant-baseline="central"><textPath href="#arc-adolescent" startOffset="50%" text-anchor="middle">ADOLESCENT</textPath></text>
    <text class="stage-label" dominant-baseline="central"><textPath href="#arc-mature" startOffset="50%" text-anchor="middle">MATURE</textPath></text>
    <text class="stage-label" dominant-baseline="central"><textPath href="#arc-dying" startOffset="50%" text-anchor="middle">DYING</textPath></text>

    <text class="copyright-note" x="642" y="735">© Copyright 2020 Harbor Academy Advisors</text>
  </g>

  <!-- Version two: solid band with direction chevrons -->
  <g class="lifecycle-panel" transform="translate(0,530)">
    <text class="brand-name" x="642" y="385">Harbor Academy Advisors</text>
    <text class="diagram-title diagram-title--grey" x="642" y="452">HAA LIFECYCLE</text>

    <use href="#wave-line" fill="none" stroke="var(--brand-blue)" stroke-width="35" stroke-linecap="round"/>

    <polyline class="chevron" points="450,585 460,595 450,605"/>
    <polyline class="chevron" points="630,585 640,595 630,605"/>
    <polyline class="chevron" points="810,585 820,595 810,605"/>

    <g class="stage-disc">
      <circle cx="366" cy="595" r="72" fill="url(#disc-fill)"/>
      <circle cx="546" cy="595" r="72" fill="url(#disc-fill)"/>
      <circle cx="727" cy="595" r="72" fill="url(#disc-fill)"/>
      <circle cx="906" cy="595" r="72" fill="url(#disc-fill)"/>
    </g>

    <text class="stage-years" x="366" y="598">0-10</text>
    <text class="stage-years" x="366" y="621">years</text>
    <text class="stage-years" x="546" y="597">10-15</text>
    <text class="stage-years" x="546" y="620">years</text>
    <text class="stage-years" x="728" y="597">15-30</text>
    <text class="stage-years" x="728" y="620">years</text>
    <text class="stage-years" x="907" y="592">20</text>
    <text class="stage-years" x="907" y="615">years+</text>

    <text class="stage-label" dominant-baseline="central"><textPath href="#arc-entrepreneur" startOffset="50%" text-anchor="middle">ENTREPRENEUR</textPath></text>
    <text class="stage-label" dominant-baseline="central"><textPath href="#arc-adolescent" startOffset="50%" text-anchor="middle">ADOLESCENT</textPath></text>
    <text class="stage-label" dominant-baseline="central"><textPath href="#arc-mature" startOffset="50%" text-anchor="middle">MATURE</textPath></text>
    <text class="stage-label" dominant-baseline="central"><textPath href="#arc-dying" startOffset="50%" text-anchor="middle">DYING</textPath></text>

    <text class="copyright-note" x="642" y="735">© Copyright 2020 Harbor Academy Advisors</text>
  </g>
</svg>
</body>
</html>
```